Harlow Brickwell Ltd- building and maintenance company looking to create professional branding for m

creation of a website for a building and maintenance company,
will need a gallery and references/ reviews page
homepage to have some company information with rolling photos of completed works
all suggestions welcome on additional requirements for website.
layout should be easy to navigate.

Target Market(s)

30-70s homeowners with mid to high income

Logo Text

Harlow Brickwell Ltd

Coding

Coded - Design and coding required

Number of Pages Required

4 page

```html
<!DOCTYPE html>
<html lang="en">
<head>
<meta charset="utf-8">
<title>Harlow Brickwell Ltd – Building &amp; Maintenance</title>
<link href="https://fonts.googleapis.com/css2?family=Roboto:ital,wght@0,300;0,400;0,500;0,700;1,400&display=swap" rel="stylesheet">
<style>
:root{
  --navy:#0d0b3e;
  --orange:#f46a12;
  --orange-dark:#e25d08;
  --text:#6a6a6a;
  --heading:#14123f;
  --grey-bg:#f2f2f2;
  --white:#ffffff;
}
*{margin:0;padding:0;box-sizing:border-box}
html,body{width:1200px;height:3607px;overflow:hidden}
body{font-family:'Roboto',sans-serif;color:var(--text);background:var(--white);position:relative}
.abs{position:absolute}
a{color:inherit;text-decoration:none}

/* top bar */
.topbar{left:0;top:0;width:1200px;height:34px;background:var(--navy);color:#fff;font-size:14px}
.topbar .social{left:112px;top:9px;display:flex;gap:16px}
.dot-icon{width:16px;height:16px;border-radius:50%;background:rgba(255,255,255,.85);display:block}
.topbar .phone{left:254px;top:8px;display:flex;align-items:center;gap:7px}
.topbar .mail{right:112px;top:7px;display:flex;align-items:center;gap:7px}

/* nav */
.nav{left:0;top:34px;width:1200px;height:66px;background:#fff;box-shadow:0 1px 4px rgba(0,0,0,.08);z-index:3}
.nav a{position:absolute;top:24px;font-size:15px;font-weight:500;color:#222}
.nav a.active{color:var(--orange)}
.nav a.active::before{content:"";position:absolute;left:8px;top:-14px;width:26px;height:2px;background:var(--orange)}
.nav .quote{left:931px;top:0;width:157px;height:66px;background:var(--orange);color:#fff;font-size:12px;font-weight:700;display:flex;align-items:center;justify-content:center;gap:6px;text-transform:uppercase}
.brand-disc{left:502px;top:-42px;width:196px;height:196px;border-radius:50%;background:#fff;z-index:4;display:flex;flex-direction:column;align-items:center;justify-content:flex-end;padding-bottom:44px}
.brand-name{font-size:16px;font-weight:700;color:var(--navy);text-align:center;line-height:1.25}
.brand-mark{width:14px;height:14px;background:var(--orange);margin-bottom:8px}

/* hero */
.hero{left:0;top:100px;width:1200px;height:670px}
.hero svg{position:absolute;left:0;top:0}
.hero-box{left:281px;top:186px;width:639px;height:257px;background:rgba(70,70,75,.38);text-align:center;color:#fff}
.hero-box h1{font-size:44px;font-weight:700;margin-top:24px;letter-spacing:.3px;text-shadow:0 2px 6px rgba(0,0,0,.25)}
.hero-box p{font-size:16px;line-height:25px;margin:18px auto 0;width:500px}
.btn-hero{left:226px;top:163px;width:186px;height:51px;border-radius:26px;background:var(--orange);color:#fff;font-size:16px;font-weight:700;display:flex;align-items:center;justify-content:center;gap:8px}

/* about */
.eyebrow{left:112px;top:838px;display:flex;align-items:center;gap:16px;color:var(--orange);font-size:18px;font-weight:500}
.eyebrow i{display:block;width:55px;height:2px;background:var(--orange)}
.about-title{left:111px;top:880px;font-size:30px;line-height:34px;font-weight:500;color:var(--heading)}
.about-text{left:111px;top:969px;width:510px;font-size:13.5px;line-height:25px}
.about-text p+p{margin-top:6px}
.btn-outline{left:110px;top:1123px;width:166px;height:45px;border:2px solid var(--orange);border-radius:23px;color:var(--orange);font-size:14px;font-weight:700;display:flex;align-items:center;justify-content:center;gap:7px}

/* services */
.services{left:0;top:1289px;width:1200px;height:702px;background:var(--grey-bg)}
.section-title{width:1200px;text-align:center;font-size:34px;font-weight:500;color:var(--heading);left:0}
.section-title em{font-style:normal;color:var(--orange)}
.underline{height:3px;background:var(--orange)}
.svc-img{top:128px;width:310px;height:190px}
.svc-card{top:293px;width:286px;height:297px;background:#fff;border-radius:6px;box-shadow:0 2px 10px rgba(0,0,0,.07);text-align:center;padding:20px 22px 0}
.svc-card h3{font-size:16.5px;font-weight:500;color:#1a1a1a;margin-bottom:15px}
.svc-card p{font-size:12.8px;line-height:21.5px;color:var(--text)}
.chev{width:30px;height:40px}

/* testimonial */
.testimonial{left:0;top:1991px;width:1200px;height:325px;background:linear-gradient(100deg,#f26a12 0%,#f57a22 45%,#f06410 100%)}
.testimonial h2{left:320px;top:56px;font-size:36px;font-weight:500;color:#fff}
.quote{left:322px;top:128px;width:680px;font-size:15px;line-height:27px;font-style:italic;color:#fff}
.client{left:322px;top:224px;color:#fff}
.client b{display:block;font-size:17px;font-weight:500}
.client span{display:block;font-size:12.5px;margin-top:6px}

/* projects */
.gal{background:#ccc}
.dots{left:580px;top:3086px;display:flex;gap:5px}
.dots i{display:block;width:10px;height:10px;border-radius:50%;background:#9a9a9a}
.dots i.on{background:#fff;border:2px solid var(--orange)}

/* footer */
.footer-shape{left:0;top:3160px}
.footer-brand{left:140px;top:3318px;width:134px;text-align:center;color:#fff}
.footer-brand .rule{width:130px;height:2px;background:#fff;margin:0 auto 8px}
.footer-brand .name{font-size:17px;font-weight:700;line-height:22px}
.reg{left:110px;top:3443px;font-size:13.5px;color:#fff}
.f-social{left:152px;top:3486px;display:flex;gap:16px}
.f-social i{display:block;width:15px;height:15px;border-radius:50%;background:#fff}
.f-col h4{font-size:16.5px;font-weight:500;color:#fff}
.f-item{display:flex;gap:10px;color:#fff;font-size:13.5px;line-height:18px}
.f-item b{display:block;font-size:11.5px;font-weight:700}
.f-links a{display:block;color:#fff;font-size:13.5px;line-height:25.7px}
.f-ask{color:#fff;font-size:12px;line-height:19px;width:240px}
.btn-foot{left:862px;top:3437px;width:198px;height:39px;border-radius:20px;background:var(--orange);color:#fff;font-size:15px;font-weight:500;display:flex;align-items:center;justify-content:center}
.goup{left:1008px;top:3520px;width:81px;height:20px;border-radius:10px;background:#fff;color:var(--navy);font-size:11px;font-weight:700;display:flex;align-items:center;justify-content:center;gap:4px}
.copyright{left:113px;top:3562px;font-size:13px;color:#fff}
.legal{right:115px;top:3562px;font-size:13px;color:#fff}
.legal span{margin:0 9px}
</style>
</head>
<body>

<!-- Top bar -->
<div class="abs topbar">
  <div class="abs social"><i class="dot-icon"></i><i class="dot-icon"></i><i class="dot-icon"></i></div>
  <div class="abs phone">
    <svg width="13" height="13" viewBox="0 0 24 24"><path fill="#fff" d="M6.6 10.8a15.1 15.1 0 0 0 6.6 6.6l2.2-2.2c.3-.3.7-.4 1-.2 1.1.4 2.3.6 3.6.6.6 0 1 .4 1 1V20c0 .6-.4 1-1 1A17 17 0 0 1 3 4c0-.6.4-1 1-1h3.5c.6 0 1 .4 1 1 0 1.3.2 2.5.6 3.6.1.3 0 .7-.2 1z"/></svg>
    0203 555 0142
  </div>
  <div class="abs mail">
    <svg width="14" height="11" viewBox="0 0 24 18"><path fill="#fff" d="M0 0h24v18H0z"/><path d="M1 1l11 9 11-9" fill="none" stroke="#0d0b3e" stroke-width="2"/></svg>
    office@harlowbrickwell.co.uk
  </div>
</div>

<!-- Navigation -->
<nav class="abs nav">
  <a class="active" style="left:112px">Home</a>
  <a style="left:179px">Design &amp; Planning</a>
  <a style="left:332px">Extensions</a>
  <a style="left:438px">HMO's</a>
  <a style="left:713px">Maintenance</a>
  <a style="left:833px">References</a>
  <a class="quote">
    <svg width="12" height="12" viewBox="0 0 24 24"><path fill="none" stroke="#fff" stroke-width="2.5" d="M4 20h4L20 8l-4-4L4 16zM14 6l4 4"/></svg>
    Get a Quote
  </a>
  <div class="abs brand-disc">
    <i class="brand-mark"></i>
    <div class="brand-name">Harlow Brickwell<br>Ltd</div>
  </div>
</nav>

<!-- Hero -->
<section class="abs hero">
  <svg width="1200" height="670" viewBox="0 0 1200 670">
    <defs>
      <linearGradient id="heroPhoto" x1="0" y1="0" x2="1" y2="1">
        <stop offset="0" stop-color="#e9e4dc"/>
        <stop offset=".45" stop-color="#cfc3b2"/>
        <stop offset=".7" stop-color="#3b3f5e"/>
        <stop offset="1" stop-color="#a8a29a"/>
      </linearGradient>
    </defs>
    <path role="img" aria-label="Photograph of a finished luxury kitchen with white cabinets, navy island and gold pendant lights" fill="url(#heroPhoto)" d="M0 0H1200V572L600 648L0 572Z"/>
    <path fill="#f46a12" d="M70 588L600 652L1130 588L600 672Z"/>
  </svg>
  <div class="abs hero-box">
    <h1>Harlow Brickwell</h1>
    <p>Harlow Brickwell Ltd provide a complete service from Design &amp; Planning Applications, Construction</p>
    <a class="abs btn-hero">GET STARTED
      <svg width="15" height="15" viewBox="0 0 24 24"><circle cx="12" cy="12" r="11" fill="#fff"/><path d="M10 7l5 5-5 5" fill="none" stroke="#f46a12" stroke-width="3"/></svg>
    </a>
  </div>
</section>

<!-- About -->
<div class="abs eyebrow"><i></i>About Us</div>
<h2 class="abs about-title">We are dedicated to providing you<br>with quality in Harlow Brickwell</h2>
<div class="abs about-text">
  <p>Harlow Brickwell Ltd provide a complete service from Design &amp; Planning Applications, Construction &amp; Structural Alterations to all finishes from Kitchens &amp; Bathrooms to Bespoke storage solutions &amp; Decor</p>
  <p>At Harlow Brickwell we pride ourselves on providing excellent customer service alongside professional high quality workmanship.</p>
</div>
<a class="abs btn-outline">LEARN MORE
  <svg width="14" height="14" viewBox="0 0 24 24"><circle cx="12" cy="12" r="11" fill="#f46a12"/><path d="M10 7l5 5-5 5" fill="none" stroke="#fff" stroke-width="3"/></svg>
</a>
<svg class="abs" style="left:690px;top:770px" width="408" height="466" viewBox="690 770 408 466">
  <defs>
    <linearGradient id="aboutPhoto" x1="0" y1="0" x2="1" y2="1">
      <stop offset="0" stop-color="#b9c2cf"/>
      <stop offset=".5" stop-color="#5c6a7e"/>
      <stop offset="1" stop-color="#e7894a"/>
    </linearGradient>
    <filter id="hexShadow"><feDropShadow dx="0" dy="2" stdDeviation="4" flood-opacity=".18"/></filter>
  </defs>
  <polygon filter="url(#hexShadow)" points="893,778 1088,890 1088,1114 893,1226 699,1114 699,890" fill="#fff"/>
  <polygon role="img" aria-label="Photograph of a site engineer in hard hat and hi-vis vest reviewing plans on a construction site" points="893,788 1080,895 1080,1109 893,1216 707,1109 707,895" fill="url(#aboutPhoto)"/>
</svg>

<!-- Services -->
<section class="abs services">
  <h2 class="abs section-title" style="top:46px"><em>Our</em> Services</h2>
  <div class="abs underline" style="left:564px;top:93px;width:72px"></div>

  <svg class="abs chev" style="left:38px;top:232px" viewBox="0 0 30 40"><path d="M22 4L8 20l14 16" fill="none" stroke="#9c9c9c" stroke-width="4"/></svg>
  <svg class="abs chev" style="left:1131px;top:232px" viewBox="0 0 30 40"><path d="M8 4l14 16L8 36" fill="none" stroke="#9c9c9c" stroke-width="4"/></svg>

  <div class="abs svc-img" role="img" aria-label="Photograph of engineers on a concrete building site" style="left:112px;background:linear-gradient(160deg,#c9ccd1,#7f8590 60%,#5b5650)"></div>
  <div class="abs svc-img" role="img" aria-label="Photograph of a detached family house with a lit porch at dusk" style="left:445px;background:linear-gradient(170deg,#8ea6b8,#4d5d72 55%,#3f5a2e)"></div>
  <div class="abs svc-img" role="img" aria-label="Photograph of a modern glass office building under a cloudy sky" style="left:778px;background:linear-gradient(170deg,#6d8aa8,#2f4a66 55%,#7e9a6a)"></div>

  <div class="abs svc-card" style="left:123px">
    <h3>Design&amp; Planning</h3>
    <p>Harlow Brickwell Design and Planning offer a free feasibility consultation, we offer Layout Plans, 3D internal design, Floor Plans &amp; Elevation drawings, Planning application submissions, Structural Calculations and Building Control Notices.</p>
  </div>
  <div class="abs svc-card" style="left:457px">
    <h3>Extensions</h3>
    <p>All types of extensions undertaken, single or double storey, garden office, loft conversions. from the smallest rear addition to a full wrap around build. we provide a comprehensive schedule of works. We make every effort to mitigate the impact on the customer and neighbours by completing projects in a timely fashion and having a full compliment of trades on site at all times.</p>
  </div>
  <div class="abs svc-card" style="left:790px">
    <h3>HMO's</h3>
    <p>Harlow Brickwell have an extensive knowledge of HMO conversions, we are able to help maximise the layout and inform landlords on the regulations and requirements needed to provide a successful HMO.</p>
  </div>
</section>

<!-- Testimonials -->
<section class="abs testimonial" role="img" aria-label="Orange tinted photograph of construction workers on site">
  <h2 class="abs">What Our Clients Have To Say</h2>
  <svg class="abs chev" style="left:106px;top:150px" viewBox="0 0 30 40"><path d="M22 4L8 20l14 16" fill="none" stroke="#fff" stroke-width="4"/></svg>
  <svg class="abs chev" style="left:1060px;top:150px" viewBox="0 0 30 40"><path d="M8 4l14 16L8 36" fill="none" stroke="#fff" stroke-width="4"/></svg>
  <svg class="abs" style="left:165px;top:100px" width="134" height="134" viewBox="0 0 134 134">
    <polygon points="67,2 132,67 67,132 2,67" fill="#fff"/>
    <polygon role="img" aria-label="Portrait photograph of the client" points="67,8 126,67 67,126 8,67" fill="#6fb3d9"/>
  </svg>
  <svg class="abs" style="left:280px;top:108px" width="34" height="26" viewBox="0 0 34 26"><text x="0" y="30" font-size="46" font-family="Georgia,serif" fill="rgba(255,255,255,.35)">“</text></svg>
  <p class="abs quote">Lorem ipsum dolor sit amet, consectetur adipiscing elit, sed do eiusmod tempor incididunt ut labore et dolore magna aliqua. Ut enim ad minim veniam, quis nostrud exercitation ullamco laboris nisi ut aliquip ex ea commodo consequat.</p>
  <svg class="abs" style="left:592px;top:186px" width="34" height="26" viewBox="0 0 34 26"><text x="0" y="30" font-size="46" font-family="Georgia,serif" fill="rgba(255,255,255,.35)">”</text></svg>
  <div class="abs client"><b>Daniel Hart</b><span>Company Name</span></div>
</section>

<!-- Completed projects -->
<h2 class="abs section-title" style="top:2408px">Completed <em>Project</em></h2>
<div class="abs underline" style="left:556px;top:2458px;width:89px"></div>

<div class="abs gal" role="img" aria-label="Photograph of a bright open-plan office with wooden floor" style="left:110px;top:2503px;width:482px;height:280px;background:linear-gradient(160deg,#f2efe9,#d9d2c5 50%,#b48a5a)"></div>
<div class="abs gal" role="img" aria-label="Photograph of a living room with fireplace and cream sofa" style="left:602px;top:2503px;width:484px;height:280px;background:linear-gradient(160deg,#e8e5df,#8c8478 50%,#4a3d33)"></div>
<div class="abs gal" role="img" aria-label="Photograph of a large family home with a green lawn" style="left:113px;top:2794px;width:322px;height:252px;background:linear-gradient(180deg,#9cc4e6,#7a7d80 55%,#4e7a3a)"></div>
<div class="abs gal" role="img" aria-label="Photograph of a lounge with cream sofas and wooden floor" style="left:445px;top:2794px;width:311px;height:252px;background:linear-gradient(160deg,#e2c9a8,#c8743a 55%,#8a4a22)"></div>
<div class="abs gal" role="img" aria-label="Photograph of a modern commercial office building" style="left:766px;top:2794px;width:320px;height:252px;background:linear-gradient(180deg,#6fa6e0,#b9bfc4 50%,#5f8a47)"></div>

<div class="abs dots"><i></i><i class="on"></i><i></i></div>

<!-- Footer -->
<svg class="abs footer-shape" width="1200" height="447" viewBox="0 3160 1200 447">
  <path fill="#f46a12" d="M80 3262L600 3171L1120 3262L600 3196Z"/>
  <path fill="#0d0b3e" d="M0 3276L600 3198L1200 3276V3607H0Z"/>
</svg>

<div class="abs footer-brand">
  <div class="rule"></div>
  <div class="name">Harlow Brickwell<br>Ltd</div>
</div>
<div class="abs reg">Registration Number- 12345678</div>
<div class="abs f-social"><i></i><i></i><i></i><i></i></div>

<div class="abs f-col" style="left:369px;top:3310px">
  <h4>Our Office Address</h4>
  <div class="f-item" style="margin-top:22px">
    <svg width="12" height="12" viewBox="0 0 24 24"><path fill="#f46a12" d="M6.6 10.8a15.1 15.1 0 0 0 6.6 6.6l2.2-2.2c.3-.3.7-.4 1-.2 1.1.4 2.3.6 3.6.6.6 0 1 .4 1 1V20c0 .6-.4 1-1 1A17 17 0 0 1 3 4c0-.6.4-1 1-1h3.5c.6 0 1 .4 1 1 0 1.3.2 2.5.6 3.6.1.3 0 .7-.2 1z"/></svg>
    <div><b>Phone</b>0203 555 0142</div>
  </div>
  <div class="f-item" style="margin-top:15px">
    <svg width="13" height="10" viewBox="0 0 24 18"><path fill="#f46a12" d="M0 0h24v18H0z"/><path d="M1 1l11 9 11-9" fill="none" stroke="#0d0b3e" stroke-width="2"/></svg>
    <div><b>Email</b>office@harlowbrickwell.co.uk</div>
  </div>
  <div class="f-item" style="margin-top:15px">
    <svg width="11" height="14" viewBox="0 0 20 26"><path fill="#f46a12" d="M10 0a10 10 0 0 1 10 10c0 7-10 16-10 16S0 17 0 10A10 10 0 0 1 10 0z"/><circle cx="10" cy="10" r="3.5" fill="#0d0b3e"/></svg>
    <div><b>Location</b>Unit 4 Meadow Court, 12 Station Road,<br>Harlow Essex CM99 1ZZ</div>
  </div>
</div>

<div class="abs f-col" style="left:672px;top:3310px">
  <h4>Company</h4>
  <div class="f-links" style="margin-top:14px">
    <a>Home</a><a>Design &amp; Planning</a><a>Extensions</a><a>HMO's</a><a>Maintenance</a><a>References</a>
  </div>
</div>

<div class="abs f-col" style="left:862px;top:3310px">
  <h4>Stil have questios?</h4>
  <p class="f-ask" style="margin-top:14px">Contact us using this form. A representative will aswer your questions as soon as possible.</p>
</div>
<a class="abs btn-foot">GET A QUOTE</a>

<a class="abs goup">
  <svg width="9" height="10" viewBox="0 0 10 12"><path d="M5 0L0 5h3v7h4V5h3z" fill="#0d0b3e"/></svg>Go Up
</a>

<div class="abs copyright">© 2021 Harlow Brickwell | All Rights Reserved</div>
<div class="abs legal">Privacy Policy<span>|</span>Cookie Policy<span>|</span>Terms Of Services</div>

</body>
</html>
```